Larkspur Ridge Management - Business Cards

I need business cards. My current logo was designed by a designer at this site and I very much like and am happy with the results. I would like a business card that is trendy, unique, current yet professional. I deal with high net worth clients daily

Target Market(s)

Out of state investors looking to get into the rental market in Ohio

Industry/Entity Type

Property Management, Consulting

Contact Information for Business Card

Name, Title (Chief Financial Officer) office phone number (555) 817-3094 website address larkridgemgmt.example

Font styles to use
Sans Serif

Colors
0054AA
0677BA
7BADD7
CADEEF
E8F1F8
0094D4
00A9DD
6FCCEA
C7EBF8
E9F6FB
00AB8E
00BBA5
67D7C9
C6EFE9
E9F9F6

```html
<!DOCTYPE html>
<html lang="en">
<head>
<meta charset="utf-8">
<title>Larkspur Ridge Management – Business Card</title>
<link rel="stylesheet" href="https://fonts.googleapis.com/css2?family=Bebas+Neue&family=Open+Sans:wght@600&display=swap">
<style>
  :root {
    --navy: #2d3f63;
    --red: #ed2027;
    --red-dark: #b3191f;
    --ink: #111111;
    --paper: #ffffff;
    --edge: #d9d9d9;
  }
  * { box-sizing: border-box; margin: 0; padding: 0; }
  html, body {
    width: 1200px; height: 1200px; overflow: hidden;
    background: var(--paper);
  }
  .card {
    position: absolute;
    left: 326px; top: 329px;
    width: 616px; height: 376px;
    background: var(--paper);
    border: 1px solid var(--edge);
    overflow: hidden;
  }
  .brand-panel {
    position: absolute; left: 0; top: 0;
    width: 284px; height: 100%;
    background: var(--navy);
    display: flex; align-items: center; justify-content: center;
    padding: 0 34px 20px 14px;
  }
  .brand-name {
    font-family: "Open Sans", sans-serif;
    font-weight: 600;
    font-size: 27px;
    line-height: 1.15;
    color: var(--paper);
    text-align: center;
    text-transform: uppercase;
    letter-spacing: 0.5px;
  }
  .contact-strip {
    position: absolute;
    left: 255px; top: 77px;
    width: 59px; height: 184px;
    box-shadow: 4px 5px 6px rgba(0,0,0,0.35);
    display: flex; flex-direction: column;
  }
  .contact-strip .cell {
    display: flex; align-items: center; justify-content: center;
    background: var(--red);
  }
  .cell.person { height: 83px; }
  .cell.phone { height: 52px; background: var(--red-dark); }
  .cell.mail { height: 49px; }
  .details {
    position: absolute;
    left: 314px; right: 0; top: 0;
    text-align: center;
    color: var(--ink);
  }
  .job-title {
    font-family: "Bebas Neue", sans-serif;
    font-weight: 400;
    font-size: 46px;
    line-height: 40px;
    margin-top: 64px;
    letter-spacing: 0.2px;
  }
  .phone-number {
    font-family: "Bebas Neue", sans-serif;
    font-size: 24px;
    margin-top: 30px;
    letter-spacing: 0.3px;
  }
  .website {
    font-family: "Open Sans", sans-serif;
    font-weight: 600;
    font-size: 20px;
    margin-top: 20px;
  }
  .brand-footer {
    position: absolute;
    left: 314px; right: 0; bottom: 22px;
    text-align: center;
    font-family: "Open Sans", sans-serif;
    font-weight: 600;
    font-size: 15px;
    color: var(--navy);
    text-transform: uppercase;
    letter-spacing: 1px;
  }
</style>
</head>
<body>
  <div class="card">
    <div class="brand-panel">
      <p class="brand-name">Larkspur Ridge Management</p>
    </div>

    <div class="contact-strip">
      <div class="cell person">
        <svg width="26" height="32" viewBox="0 0 26 32" aria-hidden="true">
          <circle cx="13" cy="8" r="7" fill="#fff"/>
          <path d="M1 31 V24 Q1 17 9 17 H17 Q25 17 25 24 V31 Z" fill="#fff"/>
        </svg>
      </div>
      <div class="cell phone">
        <svg width="36" height="36" viewBox="0 0 36 36" aria-hidden="true">
          <path d="M6 4 L11 9 L8 13 Q11 21 20 27 L24 24 L29 29 L26 32 Q14 30 4 14 Q3 8 6 4 Z" fill="none" stroke="#fff" stroke-width="2.6" stroke-linejoin="round"/>
          <rect x="4" y="2.5" width="4" height="7" transform="rotate(-45 6 6)" fill="#fff"/>
          <rect x="26" y="24.5" width="4" height="7" transform="rotate(-45 28 28)" fill="#fff"/>
        </svg>
      </div>
      <div class="cell mail">
        <svg width="38" height="24" viewBox="0 0 38 24" aria-hidden="true">
          <rect x="1.5" y="1.5" width="35" height="21" rx="2" fill="none" stroke="#fff" stroke-width="2.4"/>
          <path d="M2 3 L19 15 L36 3 M2 21 L14 11 M36 21 L24 11" fill="none" stroke="#fff" stroke-width="2.2"/>
        </svg>
      </div>
    </div>

    <div class="details">
      <h1 class="job-title">Chief<br>Financial Officer</h1>
      <p class="phone-number">(555) 817-3094</p>
      <p class="website">larkridgemgmt.example</p>
    </div>

    <p class="brand-footer">Larkspur Ridge Management</p>
  </div>
</body>
</html>
```